Need a redesign for our Wordpress Credit report website

Hi, We need someone to redesign our Wordpress credit report website, brightledgerview.co.za. The designer will be responsible for the following pages:
- home page
- blog page
- single post
- dashboard
- credit report page

About BrightLedgerView.co.za
Bright Ledger View is a consumer focussed credit report platform where South African citizens can get an easy to understand credit report that shows them where to improve their credit scores.

```html
<!DOCTYPE html>
<html lang="en">
<head>
<meta charset="utf-8">
<title>Bright Ledger View – Check Your Credit Score</title>
<link href="https://fonts.googleapis.com/css2?family=Oswald:wght@300;400;500&family=Roboto:ital,wght@0,400;0,500;1,400&display=swap" rel="stylesheet">
<style>
:root{
  --blue:#1f5fa6;
  --navy:#1c3a63;
  --green:#8cc63f;
  --green-dark:#6fae2c;
  --ink:#2b2b2b;
  --muted:#8a8f96;
  --line:#d9dde2;
  --tint:#eef3fa;
  --card:#f5f6f8;
  --gold:#f5b301;
  --white:#fff;
}
*{box-sizing:border-box;margin:0;padding:0}
html,body{width:1200px;height:4098px;overflow:hidden;background:var(--white)}
body{position:relative;font-family:"Roboto",Arial,sans-serif;color:var(--ink)}
.head{font-family:"Oswald","Arial Narrow",sans-serif;font-weight:400;text-transform:uppercase;letter-spacing:.2px}

/* header */
.site-header{position:absolute;left:0;top:0;width:1200px;height:98px}
.brand{position:absolute;left:151px;top:27px;display:flex;align-items:center;gap:10px}
.brand-dot{width:44px;height:44px;border-radius:50%;background:var(--green)}
.brand-name{font-family:"Oswald",sans-serif;font-size:21px;color:var(--navy);letter-spacing:.5px}
.nav a{position:absolute;top:46px;font-family:"Oswald",sans-serif;font-size:14px;color:var(--navy);text-decoration:none}
.btn{display:flex;align-items:center;justify-content:center;border-radius:30px;color:#fff;font-family:"Oswald",sans-serif;text-transform:uppercase;text-decoration:none}
.btn-login{position:absolute;left:943px;top:40px;width:84px;height:30px;background:var(--blue);border:2px solid var(--green);font-size:14px}

/* hero */
.hero{position:absolute;left:0;top:98px;width:1200px;height:685px;background:linear-gradient(120deg,#1f5fa6 0%,#2a86a0 38%,#6fb64a 72%,#8cc63f 100%)}
.hero h1{position:absolute;z-index:2;left:148px;top:100px;width:400px;font-size:28px;line-height:35px;font-weight:300;letter-spacing:0;color:#fff;white-space:nowrap}
.hero ul{position:absolute;left:150px;top:196px;list-style:none}
.hero li{color:#fff;font-size:14.5px;height:31px;padding-left:24px;position:relative}
.hero li::before{content:"»";position:absolute;left:0;top:-3px;font-size:19px}
.btn-hero{position:absolute;left:150px;top:339px;width:189px;height:41px;background:var(--green);font-size:14px}
.hero-visual{position:absolute;left:600px;top:98px;width:550px;height:355px;border-radius:10px;background:linear-gradient(160deg,#2b2f36 0%,#2b2f36 6%,#f3f6f3 6.5%,#e9f1e2 80%,#bfc3c8 90%,#8c9197 100%)}

/* form card */
.signup{position:absolute;left:148px;top:643px;width:904px;height:463px;background:#fff;box-shadow:0 6px 24px rgba(0,0,0,.18)}
.signup h2{position:absolute;left:0;top:44px;width:100%;text-align:center;font-size:25px;color:#1b1b1b}
.field{position:absolute;width:235px;border-bottom:1px solid var(--line);height:55px}
.field label{display:block;font-size:12px;color:#333}
.field span{display:block;margin-top:6px;font-size:15px;color:#a7abb0}
.agree{position:absolute;left:60px;top:294px;font-size:11.5px;color:#9aa0a6;display:flex;align-items:center;gap:6px}
.agree i{width:13px;height:13px;border:1px solid #b9bec4;display:inline-block}
.btn-submit{position:absolute;left:376px;top:334px;width:152px;height:45px;background:var(--blue);border:2px solid var(--green);font-size:17px;font-weight:500}
.fine{position:absolute;left:0;top:400px;width:100%;text-align:center;font-size:11px;line-height:15px;color:#8d9299}

/* features */
.section-title{position:absolute;left:0;width:1200px;text-align:center;font-size:44px;color:#1b1b1b}
.texture{position:absolute;background:#f0f1f3}
.feature{position:absolute;width:216px;height:231px;background:var(--card);text-align:center}
.feature svg{position:absolute;left:83px;top:45px}
.feature p{position:absolute;left:16px;right:16px;top:140px;font-size:14px;line-height:18px;color:#333}

/* why */
.why{position:absolute;left:0;top:1905px;width:1200px;height:621px;background:var(--tint)}
.why-card{position:absolute;top:180px;width:282px;height:336px;background:#fff;box-shadow:0 2px 10px rgba(0,0,0,.06);text-align:center}
.why-icon{position:absolute;left:95px;top:30px;width:92px;height:92px;border-radius:50%;background:var(--green)}
.why-num{position:absolute;left:90px;top:30px;width:24px;height:24px;border-radius:50%;background:var(--blue);color:#fff;font-size:13px;line-height:20px;border:2px solid #fff}
.why-card h3{position:absolute;left:20px;right:20px;top:142px;font-family:"Oswald",sans-serif;font-weight:400;font-size:17px;line-height:22px;color:#1b1b1b}
.why-card p{position:absolute;left:24px;right:24px;top:204px;font-size:11px;line-height:15px;color:#777}

/* reviews */
.reviews-title{position:absolute;left:0;top:2628px;width:1200px;text-align:center;font-size:45px}
.reviews-title .g{color:var(--green)}
.review{position:absolute;top:2737px;width:215px;height:233px;border:1px solid #e3e5e8;background:#fff;text-align:center}
.avatar{position:absolute;left:75px;top:11px;width:64px;height:64px;border-radius:50%;border:3px solid #2d2d2d}
.stars{position:absolute;left:0;width:100%;top:84px;color:var(--gold);font-size:18px;letter-spacing:2px}
.review h4{position:absolute;left:0;width:100%;top:112px;font-size:11.5px;font-weight:400;color:#333}
.review small{position:absolute;left:0;width:100%;top:127px;font-size:10.5px;color:#999}
.review p{position:absolute;left:18px;right:18px;top:150px;font-size:10.5px;line-height:14px;color:#8a8a8a;font-style:italic}
.dots{position:absolute;left:550px;top:3028px;display:flex;gap:8px}
.dots i{width:10px;height:10px;border-radius:50%;background:#d4d7db}
.dots i:first-child{background:#3a3a3a}

/* promo */
.promo{position:absolute;left:0;top:3088px;width:1200px;height:507px;background:linear-gradient(100deg,#26436a 0%,#3b5b7e 40%,#8aa3b8 65%,#c7b39a 85%,#a98466 100%)}
.promo h2{position:absolute;left:159px;top:165px;font-size:40px;line-height:47px;color:#fff}
.btn-promo{position:absolute;left:159px;top:279px;width:163px;height:41px;background:var(--blue);border:2px solid var(--green);font-size:13px}

/* app band */
.app-band{position:absolute;left:0;top:3595px;width:1200px;height:99px;background:#e9f0f8}
.app-band h3{position:absolute;left:372px;top:36px;font-size:20px;color:#1b1b1b}
.store{position:absolute;top:27px;width:150px;height:42px;background:#111;border-radius:6px;color:#fff;padding:5px 0 0 16px;border:1px solid #888}
.store small{display:block;font-size:9px;letter-spacing:.5px}
.store b{display:block;font-size:17px;font-weight:500;line-height:20px}

/* footer */
.foot-col h5{position:absolute;top:3775px;font-family:"Oswald",sans-serif;font-weight:400;font-size:19px;color:#1b1b1b}
.foot-col h5::after{content:"";position:absolute;left:0;bottom:-8px;width:62px;height:3px;background:linear-gradient(90deg,var(--blue) 50%,var(--green) 50%)}
.foot-col ul{position:absolute;top:3832px;list-style:none}
.foot-col li{font-size:11.5px;color:#8b8f95;height:24.5px;text-transform:uppercase}
.divider{position:absolute;left:778px;top:3740px;width:1px;height:255px;background:#d5d8dc}
.ask{position:absolute;left:834px;top:3768px;font-size:25px;color:#1b1b1b}
.btn-contact{position:absolute;left:850px;top:3820px;width:123px;height:40px;background:var(--blue);border:2px solid var(--green);font-size:14px}
.social{position:absolute;left:818px;top:3886px;display:flex;gap:8px}
.social span{padding:5px 9px;border-radius:14px;background:var(--blue);color:#fff;font-size:11px}
.pay{position:absolute;left:146px;top:3975px;display:flex;gap:10px}
.pay span{padding:5px 9px;border-radius:4px;background:#c7cbd0;color:#fff;font-size:11px;font-weight:500}
.copy{position:absolute;left:150px;top:4031px;font-size:11.5px;color:#555}
</style>
</head>
<body>

<header class="site-header">
  <div class="brand"><span class="brand-dot"></span><span class="brand-name">BRIGHT LEDGER VIEW</span></div>
  <nav class="nav">
    <a style="left:609px">HOME</a>
    <a style="left:682px">ARTICLES</a>
    <a style="left:775px">ABOUT</a>
    <a style="left:854px">CONTACT</a>
  </nav>
  <a class="btn btn-login">LOGIN</a>
</header>

<section class="hero">
  <h1 class="head">Banks check your credit score<br>before approving your loan</h1>
  <ul>
    <li>See your most recent credit score</li>
    <li>Get access to your full credit profile</li>
    <li>See who has been looking at your profile</li>
    <li>See if you have any adverse or Blacklistings</li>
  </ul>
  <a class="btn btn-hero">CHECK YOUR CREDIT SCORE</a>
  <div class="hero-visual" role="img" aria-label="Laptop showing a credit score dashboard with a 740 gauge and report summary"></div>
</section>

<section class="signup">
  <h2 class="head">Check your credit score within seconds - get started here</h2>
  <div class="field" style="left:60px;top:122px"><label>Id Number</label><span>Enter Your Id Number</span></div>
  <div class="field" style="left:347px;top:122px"><label>First Name</label><span>Enter Your First Name</span></div>
  <div class="field" style="left:635px;top:122px"><label>Last Name</label><span>Enter Your Last Name</span></div>
  <div class="field" style="left:60px;top:215px"><label>Primary Email</label><span>Enter Your Email</span></div>
  <div class="field" style="left:347px;top:215px"><label>Mobile Number</label><span>Enter Your Phone number</span></div>
  <div class="field" style="left:635px;top:215px"><label>Date Of Birth</label><span>Enter Your DOB</span></div>
  <div class="agree"><i></i>I agree with the terms and conditions</div>
  <a class="btn btn-submit">SUBMIT</a>
  <p class="fine">By signing up and agreeing with the terms you authorise BrightLedgerView.co.za<br>to request your credit report from the bureaus and display it within the site.</p>
</section>

<h2 class="section-title head" style="top:1196px">System Features</h2>
<div class="texture" style="left:867px;top:1451px;width:231px;height:236px" role="img" aria-label="Dotted background texture"></div>
<div class="texture" style="left:127px;top:1587px;width:236px;height:238px" role="img" aria-label="Dotted background texture"></div>

<div class="feature" style="left:148px;top:1302px">
  <svg width="50" height="50" viewBox="0 0 50 50" fill="none" stroke-width="2.5"><circle cx="14" cy="18" r="6" stroke="var(--blue)"/><circle cx="36" cy="18" r="6" stroke="var(--green)"/><path d="M3 42c0-8 5-13 11-13s11 5 11 13z" stroke="var(--blue)"/><path d="M25 42c0-8 5-13 11-13s11 5 11 13z" stroke="var(--green)"/><path d="M26 6l-3 8h5l-3 8" stroke="var(--blue)"/></svg>
  <p>Dispute generator - easily manage disputes</p>
</div>
<div class="feature" style="left:377px;top:1302px">
  <svg width="50" height="50" viewBox="0 0 50 50" fill="none" stroke-width="2.5"><circle cx="25" cy="25" r="21" stroke="var(--blue)"/><circle cx="25" cy="25" r="14" stroke="var(--green)"/><path d="M29 19c-1-2-7-2-7 1s7 2 7 6-6 4-8 1M25 15v20" stroke="var(--blue)"/></svg>
  <p>Budget tool - easily create a budget</p>
</div>
<div class="feature" style="left:608px;top:1302px">
  <svg width="50" height="50" viewBox="0 0 50 50" fill="none" stroke-width="3"><path d="M5 38a20 20 0 0 1 40 0" stroke="var(--blue)"/><path d="M30 20a20 20 0 0 1 15 18" stroke="var(--green)"/><path d="M25 38l8-14" stroke="var(--blue)"/><circle cx="25" cy="38" r="3" fill="var(--blue)"/></svg>
  <p>Improve your credit score eBook</p>
</div>
<div class="feature" style="left:839px;top:1302px">
  <svg width="50" height="50" viewBox="0 0 50 50" fill="none" stroke-width="2.5"><rect x="10" y="4" width="30" height="42" rx="2" stroke="var(--blue)"/><path d="M16 16h18M16 23h18M16 30h18M16 37h18M25 16v21" stroke="var(--green)"/></svg>
  <p>Personal Budgeting Spreadsheet</p>
</div>
<div class="feature" style="left:261px;top:1549px">
  <svg width="50" height="50" viewBox="0 0 50 50" fill="none" stroke-width="2.5"><rect x="16" y="4" width="30" height="24" stroke="var(--blue)"/><path d="M28 11l8 5-8 5z" fill="var(--green)"/><rect x="4" y="22" width="28" height="20" stroke="var(--blue)"/><path d="M2 46h46" stroke="var(--green)"/></svg>
  <p>Perfect score video course</p>
</div>
<div class="feature" style="left:492px;top:1549px">
  <svg width="50" height="50" viewBox="0 0 50 50" fill="none" stroke-width="2.5"><rect x="8" y="14" width="34" height="26" stroke="var(--blue)"/><path d="M15 34v-6M21 34v-10M27 34v-8M33 34v-12" stroke="var(--green)"/><rect x="18" y="2" width="14" height="10" stroke="var(--green)"/><path d="M4 44h42" stroke="var(--blue)"/></svg>
  <p>Personal Finance Video Tutorials</p>
</div>
<div class="feature" style="left:723px;top:1549px">
  <svg width="50" height="50" viewBox="0 0 50 50" fill="none" stroke-width="2.5"><circle cx="25" cy="17" r="9" stroke="var(--blue)"/><path d="M13 18a12 12 0 0 1 24 0" stroke="var(--green)"/><path d="M8 46c0-10 8-16 17-16s17 6 17 16" stroke="var(--blue)"/><path d="M37 20v4h-8" stroke="var(--green)"/></svg>
  <p>Dedicated 24/7 Support</p>
</div>

<section class="why">
  <h2 class="section-title head" style="top:90px">Why get your score from us?</h2>
  <div class="why-card" style="left:150px">
    <div class="why-icon"><svg width="92" height="92" viewBox="0 0 92 92" fill="none" stroke="#fff" stroke-width="2"><rect x="30" y="32" width="32" height="28"/><path d="M30 38h32M36 46h8M36 52h8M48 44h9v10h-9z"/></svg></div>
    <span class="why-num">1</span>
    <h3>We don't abuse your<br>personal information:</h3>
    <p>Companies that give out free credit scores use your personal information to sell you financial products. That's how they can afford to give it to you for free. We believe that your personal information should be protected and not abused. That's why we ask a small fee. It enables us to protect your information and not abuse it.</p>
  </div>
  <div class="why-card" style="left:459px">
    <div class="why-icon"><svg width="92" height="92" viewBox="0 0 92 92" fill="none" stroke="#fff" stroke-width="2"><path d="M30 60h34M34 60V50M41 60V44M48 60V48M55 60V38M32 44l10-8 7 5 12-10"/></svg></div>
    <span class="why-num">2</span>
    <h3>Our report is super easy<br>to understand:</h3>
    <p>Our credit report is one of the easiest reports to understand. The report is clearly laid out and you will see immediately if you can apply for finance, if you are blacklisted, and where you can improve.</p>
  </div>
  <div class="why-card" style="left:767px">
    <div class="why-icon" role="img" aria-label="Outline map of Africa"><svg width="92" height="92" viewBox="0 0 92 92"><ellipse cx="46" cy="46" rx="13" ry="17" fill="#fff"/></svg></div>
    <span class="why-num">3</span>
    <h3>300,000 + South Africans<br>have trusted us:</h3>
    <p>Since 2008 we have helped over 300,000 South Africans make sense of their credit reports, so you can rest assured knowing that we have a proven track record and that you are in safe hands with us.</p>
  </div>
</section>

<h2 class="reviews-title head"><span class="g">Verified Reviews</span> &nbsp;/&nbsp; Client Testimonials</h2>
<div class="review" style="left:127px">
  <div class="avatar" style="background:#9a8a7c" role="img" aria-label="Reviewer profile photo"></div>
  <div class="stars">★★★★★</div><h4>Lerato Mokoena</h4><small>28 reviews</small>
  <p>The credit report is easy to use, informative and accurate to the date. Helps me to manage my financial well-being.</p>
</div>
<div class="review" style="left:371px">
  <div class="avatar" style="background:#b08562" role="img" aria-label="Reviewer profile photo"></div>
  <div class="stars">★★★★★</div><h4>Janine du Plessis</h4><small>2 reviews</small>
  <p>Their customer support team has been very impressive. The tools and knowledge they shared were of great practical use.</p>
</div>
<div class="review" style="left:614px">
  <div class="avatar" style="background:#1f63c9;color:#fff;font-size:28px;line-height:58px">P</div>
  <div class="stars">★★★★★</div><h4>Pieter Naidoo</h4><small>7 reviews</small>
  <p>This app is easy to use and efficient, and it was very quick to join.Also very helpful.</p>
</div>
<div class="review" style="left:858px">
  <div class="avatar" style="background:#4d6b3a" role="img" aria-label="Reviewer profile photo"></div>
  <div class="stars">★★★★★</div><h4>Summit Fitness SA</h4><small>2 reviews</small>
  <p>Excellent credit report service. They respond to queries promptly and have a very detailed credit report which is helpful and informative</p>
</div>
<div class="dots"><i></i><i></i><i></i><i></i><i></i><i></i></div>

<section class="promo" role="img" aria-label="Hand holding a phone showing a credit score of 752 with payment history, credit usage and credit age">
  <h2 class="head">Get your credit score<br>&amp; report today.</h2>
  <a class="btn btn-promo">GET STARTED NOW</a>
</section>

<section class="app-band">
  <h3 class="head">Download your app</h3>
  <div class="store" style="left:608px"><small>GET IT ON</small><b>AppShelf</b></div>
  <div class="store" style="left:764px"><small>Download on the</small><b>PocketStore</b></div>
</section>

<footer>
  <div class="foot-col"><h5 style="left:150px">TERMS</h5><ul style="left:150px"><li>General terms of use</li><li>Exclusion of liability</li><li>Security policy</li><li>Privacy policy</li></ul></div>
  <div class="foot-col"><h5 style="left:380px">PURCHASE</h5><ul style="left:380px"><li>Delivery policy</li><li>Data policy</li><li>Refund policy</li><li>Charges and fees</li></ul></div>
  <div class="foot-col"><h5 style="left:594px">QUICK LINKS</h5><ul style="left:594px"><li>About us</li><li>Articles</li><li>Contact us</li><li>Login</li></ul></div>
  <div class="divider"></div>
  <h3 class="ask head">Have questions ?</h3>
  <a class="btn btn-contact">CONTACT US</a>
  <div class="social"><span>Chatter</span><span>Flit</span><span>Tubely</span><span>Linkfolk</span></div>
  <div class="pay"><span>Cardex</span><span>Paynet</span><span>Maxcard</span><span>Vera</span></div>
  <p class="copy">© All Rights Reserved BrightLedgerView.co.za | NCR Reg. No. NCRCB97</p>
</footer>

</body>
</html>
```